Velto Works CBD Packaging Label Design. Creative Modern Minimalist. Future Work possible!!!

Creating a CBD product.Bottle size is height 84mm diameter 25mmLabel size 74mm x 38mmMatch Stick Box: 40mm x 100mm x 50mm
Pippette cap is red FYI.
NOTE: We have added a logo file but I am also paying for a new logo design. So do as you please.Need the packaging and labelling done for CBD product. Name is Velto Works. Logo is included in file below. I have also added some product packaging and design for inspiration. No need to use this but to give you an idea. Some flexibility with label dimensions. In so far as, it must fit on the base of the bottle, think eye dropper.

The last brimloft cbd oil dropper is a cool industrial design but we would prefer a design with a label.Red and white are the main colors. Minimalist, modern, clean, swiss cross in the mix are acceptable.

Also, the logo image with the textured background on the business card is part of then look we would like to package. Not a requirement but certainly a consideration.Feel free to reach out for any further questions.Below are some specs and text we need to squeeze on then packaging / labelling.

The location of the text or emphasis is NOT fixed even if it specifies the location in the description below.

Box must contain:
logo, velto Works text
Warnings-(warning sign with exclamation mark) not suitable for consumption -under 18 restricted sign?
PACKAGING TEXT (Classic rectangular)
LogoCanna Labs (below logo)10% CBD Oil (x milligram mg)10ml
Disclaimers (From dorvexi)
MEDICAL: (From dorvexi website) Disclaimer: Velto Works products are sold without any medical claims; they have not been proven to treat, relieve, nor cure any disease or medical condition. please refer to the terms and conditions (need to read these from)
CONTACT: Avoid contact during pregnancy and while nursing. Do not get in eyes, on skin, or on clothing. Get medical advice/attention if you feel unwell.ADVICE: Keep out of reach of children. Protect from sunlight. Store in a well-ventilated place. Keep cool. Refrigerate after opening.
Ingredients: Ingredients: 80% MCT oil, 20% Carmagnola Selezionata (What terpenes?check with clear horizon). 100% organic. (Check labeling) Extracted using ethanol extraction.

Side note: More information about boxing size and bottle can be seen on a competitiors site. shown below.

https://dorvexi.example/product-category/selection/

Target Market(s)

CBD oil users in Europe

Logo Text

velto works

Font styles to use
Serif
Sans Serif
Script

Requirements
Must have
• I want textured, like business card texture considered for the label. The box is a standard cardboard for the moment. Pharma grade product. I would like it to stand out in a pharmacy but not look out of place.
• We need all sides of the packaging. Use lorem ipsum if you have to. Some of the text is above though
Should not have
• Nothing that references the weed leaf. Keep that off

```html
<!DOCTYPE html>
<html lang="en">
<head>
<meta charset="utf-8">
<title>Velto Works – 10% CBD Oil Packaging</title>
<link rel="stylesheet" href="https://fonts.googleapis.com/css2?family=Bebas+Neue&family=Roboto:ital,wght@0,300;0,400;0,500;1,400;1,700&display=swap">
<style>
  :root {
    --backdrop: #d4d4d4;
    --paper: #ffffff;
    --paper-shade: #ececec;
    --ink: #1c1c1c;
    --ink-deep: #161616;
    --red: #e0241f;
    --white: #ffffff;
  }
  * { box-sizing: border-box; margin: 0; padding: 0; }
  html, body { width: 1200px; height: 801px; overflow: hidden; }
  body {
    background: var(--backdrop);
    font-family: "Roboto", Arial, sans-serif;
    color: var(--ink);
    position: relative;
  }
  .panel {
    position: absolute;
    display: flex;
    flex-direction: column;
    box-shadow: 0 6px 18px rgba(0,0,0,.12);
  }
  .panel__top {
    background:
      repeating-linear-gradient(45deg, rgba(0,0,0,.012) 0 2px, transparent 2px 4px),
      linear-gradient(160deg, var(--paper) 40%, var(--paper-shade));
  }
  .panel__band { height: 8px; background: var(--red); flex: none; }
  .panel__bottom {
    color: var(--white); flex: 1;
    background:
      repeating-linear-gradient(45deg, rgba(255,255,255,.015) 0 2px, transparent 2px 4px),
      linear-gradient(160deg, var(--ink) 40%, var(--ink-deep));
  }

  .brand {
    display: flex; align-items: center; gap: 8px;
    font-weight: 300; color: var(--ink); letter-spacing: .2px; white-space: nowrap;
  }
  .brand__dot { width: 12px; height: 12px; border-radius: 50%; background: var(--red); flex: none; }

  .swiss-cross { display: block; }

  /* Box top flap */
  .box-top {
    left: 150px; top: 112px; width: 270px; height: 70px;
    justify-content: center; align-items: center;
  }
  .box-top .brand { font-size: 14px; }
  .box-top .brand__dot { width: 8px; height: 8px; }

  /* Box front */
  .box-front { left: 150px; top: 182px; width: 270px; height: 540px; }
  .box-front .panel__top { height: 262px; padding: 40px 0 0 20px; position: relative; }
  .box-front .brand { font-size: 25px; }
  .box-front .brand__dot { width: 14px; height: 14px; }
  .strength { font-family: "Bebas Neue", Impact, sans-serif; font-size: 30px; line-height: 1; margin: 56px 0 0 28px; }
  .product-word { font-family: "Bebas Neue", Impact, sans-serif; line-height: .85; letter-spacing: 1px; }
  .box-front .product-word--cbd { position: absolute; left: 28px; bottom: 4px; font-size: 98px; }
  .box-front .product-word--cbd .swiss-cross { position: absolute; left: 24px; top: 28px; }
  .box-front .panel__bottom { padding: 12px 0 0 28px; }
  .box-front .product-word--oil { font-size: 98px; color: var(--white); }
  .spec { margin-top: 34px; text-align: center; width: 104px; }
  .spec__type { font-size: 14px; font-weight: 300; white-space: nowrap; }
  .spec__dose { font-family: "Bebas Neue", Impact, sans-serif; font-size: 28px; color: var(--red); letter-spacing: 4px; margin-top: 2px; white-space: nowrap; }
  .origin { margin-top: 22px; text-align: center; width: 104px; }
  .origin .swiss-cross { margin: 0 auto 8px; }
  .origin__line { font-size: 12px; font-weight: 300; letter-spacing: .5px; white-space: nowrap; line-height: 1.3; }
  .origin__line--strong { font-weight: 500; }

  /* Box side */
  .box-side { left: 420px; top: 182px; width: 270px; height: 540px; }
  .box-side .panel__top { height: 262px; padding: 40px 22px 0 20px; }
  .box-side .panel__bottom { padding: 16px 22px 0 20px; position: relative; }
  .copy { font-size: 11.5px; line-height: 1.45; margin-bottom: 16px; }
  .copy__label { color: var(--red); font-style: italic; font-weight: 700; }
  .copy__accent { color: var(--red); }
  .box-side .brand { position: absolute; left: 20px; bottom: 20px; font-size: 11px; color: var(--white); gap: 5px; }
  .box-side .brand__dot { width: 7px; height: 7px; }

  /* Bottle label */
  .bottle-label { left: 830px; top: 270px; width: 220px; height: 330px; }
  .bottle-label .panel__top { height: 180px; padding: 30px 0 0 22px; position: relative; }
  .bottle-label .brand { font-size: 19px; }
  .bottle-label .brand__dot { width: 11px; height: 11px; }
  .bottle-label .strength { font-size: 24px; margin: 22px 0 0 26px; }
  .bottle-label .product-word--cbd { position: absolute; left: 26px; bottom: 4px; font-size: 66px; }
  .bottle-label .product-word--cbd .swiss-cross { position: absolute; left: 16px; top: 19px; }
  .bottle-label .panel__bottom { padding: 6px 0 0 26px; }
  .bottle-label .product-word--oil { font-size: 66px; color: var(--white); }
  .bottle-label .spec__dose { font-size: 22px; margin-top: 4px; text-align: left; }
</style>
</head>
<body>

<section class="panel box-top panel__top" aria-label="Box top flap">
  <div class="brand"><span class="brand__dot"></span>Velto Works</div>
</section>

<section class="panel box-front" aria-label="Box front panel">
  <div class="panel__top">
    <div class="brand"><span class="brand__dot"></span>Velto Works</div>
    <p class="strength">10%</p>
    <p class="product-word product-word--cbd">CBD
      <svg class="swiss-cross" width="16" height="16" viewBox="0 0 16 16" aria-hidden="true"><rect width="16" height="16" fill="#e0241f"/><rect x="6.5" y="3" width="3" height="10" fill="#fff"/><rect x="3" y="6.5" width="10" height="3" fill="#fff"/></svg>
    </p>
  </div>
  <div class="panel__band"></div>
  <div class="panel__bottom">
    <p class="product-word product-word--oil">OIL</p>
    <div class="spec">
      <p class="spec__type">Full Spectrum</p>
      <p class="spec__dose">1000 MG</p>
    </div>
    <div class="origin">
      <svg class="swiss-cross" width="18" height="18" viewBox="0 0 16 16" aria-hidden="true"><rect width="16" height="16" fill="#e0241f"/><rect x="6.5" y="3" width="3" height="10" fill="#fff"/><rect x="3" y="6.5" width="10" height="3" fill="#fff"/></svg>
      <p class="origin__line">SWISS MADE</p>
      <p class="origin__line origin__line--strong">CANABINOIDS</p>
    </div>
  </div>
</section>

<section class="panel box-side" aria-label="Box side panel">
  <div class="panel__top">
    <p class="copy"><span class="copy__label">Disclaimer:</span> Velto Works products are sold without any medical claims; they have not been proven to treat, relieve, nor cure any disease or medical condition. please refer to the terms and conditions (need to read these from)</p>
    <p class="copy"><span class="copy__label">CONTACT:</span> Avoid contact during pregnancy and while nursing. Do not get in eyes, on skin, or on clothing. Get medical advice/attention if you feel unwell.</p>
  </div>
  <div class="panel__band"></div>
  <div class="panel__bottom">
    <p class="copy"><span class="copy__label">ADVICE:</span> Keep out of reach of children. Protect from sunlight. Store in a well-ventilated place. Keep cool. Refrigerate after opening.</p>
    <p class="copy"><span class="copy__label">Ingredients:</span> Ingredients: <span class="copy__accent">80%</span> MCT oil, 20% Carmagnola Selezionata (What terpenes?-check with clear horizon). <span class="copy__accent">100% organic.</span> (Check labeling) Extracted using ethanol extraction.</p>
    <div class="brand"><span class="brand__dot"></span>Velto Works</div>
  </div>
</section>

<section class="panel bottle-label" aria-label="Bottle label">
  <div class="panel__top">
    <div class="brand"><span class="brand__dot"></span>Velto Works</div>
    <p class="strength">10%</p>
    <p class="product-word product-word--cbd">CBD
      <svg class="swiss-cross" width="12" height="12" viewBox="0 0 16 16" aria-hidden="true"><rect width="16" height="16" fill="#e0241f"/><rect x="6.5" y="3" width="3" height="10" fill="#fff"/><rect x="3" y="6.5" width="10" height="3" fill="#fff"/></svg>
    </p>
  </div>
  <div class="panel__band"></div>
  <div class="panel__bottom">
    <p class="product-word product-word--oil">OIL</p>
    <p class="spec__dose">1000 MG</p>
  </div>
</section>

</body>
</html>
```